ambitious event and festival agency from austria needs fresh business card design

A new design is due for the new headquarters and the new challenges. We organize events for different target groups from 16 to 60 years. The design should therefore be straightforward and not confused, so we are open to new colors and the logo may also be changed. In general, however, the most interesting suggestions are the most interesting ones. after this order we are looking for more graphics for partyvelt facebook instagramm homepage etc A new design is due for the new headquarters and the new challenges. We organize events for different target groups from 16 to 60 years. The design should therefore be straightforward and not confused, so we are open to new colors and the logo may also be changed. In general, however, the most interesting suggestions are the most interesting ones. after this order we are looking for more graphics for partyvelt facebook instagramm homepage etc A new design is due for the new headquarters and the new challenges. We organize events for different target groups from 16 to 60 years. The design should therefore be straightforward and not confused, so we are open to new colors and the logo may also be changed. In general, however, the most interesting suggestions are the most interesting ones. after this order we are looking for more graphics for partyvelt facebook instagramm homepage etc

Reason: I am sorry for this decision but i need some more time. No new designs please, there are so many good ones and I will have made a decision in the next 3 days.

Target Market(s)

Industry/Entity Type

Business

Font styles to use
Serif
Sans Serif

Colors

Designer to choose colors to be used in the design.

Requirements
Must have
Nice to have
Should not have

```html
<!DOCTYPE html>
<html lang="en">
<head>
<meta charset="utf-8">
<title>partyvelt – Business Card</title>
<link href="https://fonts.googleapis.com/css2?family=Open+Sans:wght@400;600;700&display=swap" rel="stylesheet">
<style>
  :root {
    --stage: #000000;
    --card: #ffffff;
    --ink: #1e1e1e;
    --grey: #5d6365;
    --red: #b3203a;
    --photo-top: #5fc4ea;
    --photo-mid: #4a7fd6;
    --photo-low: #8a3fc2;
    --photo-base: #3b1a5c;
  }
  * { margin: 0; padding: 0; box-sizing: border-box; }
  html, body { width: 1200px; height: 900px; overflow: hidden; background: var(--stage); }
  body { position: relative; font-family: "Open Sans", Arial, sans-serif; color: var(--ink); }

  .card { position: absolute; top: 275px; width: 477px; height: 293px; overflow: hidden; }

  .card--front { left: 116px; background: var(--card); border-radius: 0 62px 0 62px; }
  .card--back  { left: 622px; top: 276px; height: 292px; border-radius: 62px 0 62px 0; }

  .holder { position: absolute; right: 20px; top: 35px; text-align: right; }
  .holder__name { font-size: 19px; font-weight: 600; color: var(--grey); line-height: 1.1; }
  .holder__name span { color: var(--red); }
  .holder__role { font-size: 12.5px; color: var(--ink); margin-top: 3px; }

  .wordmark { position: absolute; display: flex; align-items: center; gap: 8px;
    font-weight: 600; letter-spacing: -1.5px; line-height: 1; }
  .wordmark__mark { width: 14px; height: 14px; flex: none; }
  .card--front .wordmark { left: 47px; top: 78px; font-size: 60px; color: var(--grey); }
  .card--front .wordmark__mark { background: var(--red); }
  .card--back .wordmark { left: 78px; top: 206px; font-size: 58px; color: #ffffff; }
  .card--back .wordmark__mark { background: #ffffff; }

  .address { position: absolute; right: 21px; top: 157px; text-align: right;
    font-size: 13px; line-height: 17px; font-style: normal; }

  .contacts { position: absolute; right: 20px; top: 216px; list-style: none; font-size: 13px; line-height: 17.5px; }
  .contacts li { display: flex; justify-content: flex-end; align-items: center; gap: 7px; }
  .contacts svg { width: 10px; height: 10px; fill: var(--red); }

  .stage-photo { position: absolute; inset: 0;
    background:
      radial-gradient(ellipse 40% 35% at 88% 30%, rgba(255,255,255,.75), transparent 70%),
      radial-gradient(ellipse 30% 30% at 15% 15%, rgba(220,245,255,.7), transparent 70%),
      linear-gradient(180deg, var(--photo-top) 0%, var(--photo-mid) 40%, var(--photo-low) 75%, var(--photo-base) 100%); }
</style>
</head>
<body>
  <section class="card card--front">
    <div class="holder">
      <p class="holder__name">Martin <span>Keller</span></p>
      <p class="holder__role">Managing Director</p>
    </div>
    <div class="wordmark"><span class="wordmark__mark"></span>partyvelt</div>
    <address class="address">48 Lindengasse Street<br>Vienna, Austria 1070</address>
    <ul class="contacts">
      <li>043-518 274 960
        <svg viewBox="0 0 10 10"><path d="M2 0.5 L3.6 2.6 L2.7 3.6 Q3.8 5.9 6.3 7.2 L7.4 6.3 L9.5 7.9 L8.4 9.6 Q4.3 9.4 1.6 5.8 Q0.3 3.6 0.5 1.6 Z"/></svg></li>
      <li>hello@partyvelt.at
        <svg viewBox="0 0 10 10"><path d="M0 1.8 H10 V8.2 H0 Z M0.8 2.4 L5 5.4 L9.2 2.4" stroke="#fff" stroke-width="0.9"/></svg></li>
      <li>www.partyvelt.at
        <svg viewBox="0 0 10 10"><path d="M4.2 5.8 L5.8 4.2 M3.8 3.6 L5.4 2 Q6.9 0.6 8.3 2 Q9.5 3.3 8.1 4.7 L6.5 6.3 M6.2 6.4 L4.6 8 Q3.1 9.4 1.7 8 Q0.5 6.7 1.9 5.3 L3.5 3.7" stroke="var(--red)" stroke-width="1.2" fill="none"/></svg></li>
    </ul>
  </section>

  <section class="card card--back">
    <div class="stage-photo" role="img" aria-label="Photo of a concert crowd with raised hands in front of a lit stage with blue and purple lights"></div>
    <div class="wordmark"><span class="wordmark__mark"></span>partyvelt</div>
  </section>
</body>
</html>
```